Web form face-lift for an online startup

We are a web startup building a SaaS application for the freight industry. The project is mainly dedicated to the paint the main form that our customer are using along the search results that the they get. All details are in the attached documents.
Updates
The application serves the Freight Forwarders community so please think towards this industry when using background images, banners, colors, icons, etc. Computer and technology images are irrelevant.
Customer fields at the top of the page is actually part of the form.
Target Market(s)
Usually business users (Sales people, procurement, shippers, freight forwarders). Some are less tech savvy and some appreciate the new trendy web apps.
Industry/Entity Type
Building
Colors
Designer to choose colors to be used in the design.
Look and feel
Each slider illustrates characteristics of the customer's brand and the style your logo design should communicate.

```html
<!DOCTYPE html>
<html lang="en">
<head>
<meta charset="utf-8">
<title>SAAS application — Search for Quotes</title>
<link rel="stylesheet" href="https://fonts.googleapis.com/css2?family=Montserrat:wght@400;500;600;700&display=swap">
<style>
  :root {
    --bar: #2d2d2d;
    --bar-text: #e6e6e6;
    --bar-muted: #b5b5b5;
    --page: #f4f4f4;
    --card: #efefef;
    --card-border: #d6d6d6;
    --field: #ffffff;
    --field-border: #d2d2d2;
    --select: #e9e9e9;
    --ink: #2b2b2b;
    --muted: #9a9a9a;
    --accent: #f08a00;
    --button-top: #ffd36a;
    --button-bottom: #f6a91c;
    --map-light: #b9b9b9;
    --map-dark: #9f9f9f;
    --go: #6cc21f;
    --hazard: #d2242c;
  }
  * { box-sizing: border-box; margin: 0; padding: 0; }
  html, body { width: 1200px; height: 965px; overflow: hidden; }
  body {
    position: relative;
    background: var(--page);
    font-family: "Montserrat", Arial, sans-serif;
    color: var(--ink);
    font-size: 12px;
  }
  .abs { position: absolute; }

  /* Header */
  .site-header { position: absolute; left: 0; top: 0; width: 1200px; height: 66px; background: var(--bar); }
  .brand { left: 161px; top: 18px; color: #fff; font-size: 24px; font-weight: 400; letter-spacing: .2px; }
  .brand b { font-weight: 700; }
  .utility { top: 10px; font-size: 11px; color: var(--bar-muted); }
  .utility .caret { font-size: 8px; margin-left: 2px; }
  .utility.user { color: var(--accent); }
  .nav-mark { left: 475px; top: 31px; width: 27px; height: 27px; border-radius: 50%; border: 3px solid #6fa8dc; background: #fff; }
  .nav-item { top: 38px; color: var(--bar-text); font-size: 11.5px; font-weight: 500; }

  /* Cards */
  .card { background: var(--card); border: 1px solid var(--card-border); border-radius: 3px; box-shadow: 0 1px 2px rgba(0,0,0,.08); }
  .search-card { left: 162px; top: 107px; width: 875px; height: 70px; background: linear-gradient(#fafafa,#eeeeee); }
  .search-title { left: 176px; top: 132px; font-size: 19px; font-weight: 500; }
  .label { font-size: 11.5px; font-weight: 600; color: var(--ink); }
  .field { position: absolute; background: var(--field); border: 1px solid var(--field-border); border-radius: 3px; font-size: 11px; color: var(--muted); padding-left: 9px; display: flex; align-items: center; }
  .field.center { justify-content: center; padding-left: 0; }
  .check { position: absolute; width: 12px; height: 12px; background: #fff; border: 1px solid #c4c4c4; border-radius: 2px; }
  .select { position: absolute; background: linear-gradient(#f5f5f5,#e2e2e2); border: 1px solid var(--field-border); border-radius: 3px; font-size: 11px; color: var(--ink); display: flex; align-items: center; padding-left: 10px; }
  .select::after { content: ""; position: absolute; right: 10px; top: 50%; margin-top: -2px; border: 4px solid transparent; border-top: 5px solid #666; }

  /* Load type tabs */
  .tab { position: absolute; top: 217px; height: 62px; background: #f9f9f9; border: 1px solid var(--card-border); border-bottom: none; border-radius: 3px 3px 0 0; }
  .tab.active { background: var(--card); height: 63px; z-index: 2; }
  .tab-art { position: absolute; left: 12px; top: 14px; width: 52px; height: 38px; border-radius: 3px; }
  .link { color: var(--accent); font-weight: 600; font-size: 12px; }
  .load-panel { left: 162px; top: 278px; width: 875px; height: 217px; }
  .add-units { left: 178px; top: 385px; width: 108px; height: 30px; border-radius: 3px; background: linear-gradient(var(--button-top),var(--button-bottom)); border: 1px solid #e59a12; font-size: 11px; font-weight: 600; display: flex; align-items: center; justify-content: center; }
  .divider { left: 178px; top: 430px; width: 844px; height: 1px; background: #dcdcdc; border-bottom: 1px solid #fff; }
  .unit-tag { position: absolute; top: 0; right: 0; height: 100%; background: linear-gradient(#f5f5f5,#e2e2e2); border-left: 1px solid var(--field-border); color: var(--ink); display: flex; align-items: center; padding-left: 8px; border-radius: 0 3px 3px 0; }
  .unit-tag::after { content: ""; position: absolute; right: 8px; top: 50%; margin-top: -2px; border: 4px solid transparent; border-top: 5px solid #666; }

  /* Route band */
  .route-band { left: 0; top: 542px; width: 1200px; height: 153px; background: linear-gradient(135deg,var(--map-light),var(--map-dark) 50%,var(--map-light)); }
  .route-label { top: 610px; font-size: 15px; font-weight: 700; color: var(--ink); }
  .route-field { top: 600px; height: 38px; box-shadow: 0 1px 3px rgba(0,0,0,.2); }

  /* Options */
  .options-title { left: 162px; top: 730px; font-size: 20px; font-weight: 500; }
  .radio { position: absolute; top: 763px; width: 13px; height: 13px; border-radius: 50%; background: #fff; border: 1px solid #c4c4c4; }
  .opt-text { top: 763px; font-size: 11.5px; font-weight: 500; }
  .hazard { position: absolute; top: 761px; }

  .search-button { left: 433px; top: 835px; width: 186px; height: 49px; border-radius: 25px; background: linear-gradient(var(--button-top),var(--button-bottom)); border: 1px solid #e9a017; box-shadow: 0 2px 3px rgba(0,0,0,.18); font-size: 15px; font-weight: 700; color: #3a2a05; display: flex; align-items: center; justify-content: center; letter-spacing: .3px; }

  /* Footer */
  .site-footer { position: absolute; left: 0; top: 923px; width: 1200px; height: 42px; background: var(--bar); }
  .footer-link { top: 937px; font-size: 11px; color: var(--bar-text); }
  .social { position: absolute; top: 937px; width: 15px; height: 15px; border-radius: 3px; background: #9a9a9a; }
</style>
</head>
<body>

<header class="site-header"></header>
<div class="abs brand"><b>SAAS</b> application</div>
<div class="abs utility" style="left:875px">USD<span class="caret">▼</span></div>
<div class="abs utility" style="left:919px">English<span class="caret">▼</span></div>
<div class="abs utility user" style="left:983px">User name</div>
<div class="abs nav-mark"></div>
<nav>
  <span class="abs nav-item" style="left:523px">Menu Item 1</span>
  <span class="abs nav-item" style="left:613px">Menu Item 2</span>
  <span class="abs nav-item" style="left:702px">Menu Item 3</span>
  <span class="abs nav-item" style="left:789px">Menu Item 4</span>
  <span class="abs nav-item" style="left:877px">Menu Item 5</span>
  <span class="abs nav-item" style="left:972px">Menu Item 6</span>
</nav>

<!-- Search for quotes -->
<section class="abs card search-card"></section>
<h1 class="abs search-title">Search for Quotes</h1>
<span class="abs label" style="left:390px;top:135px">Customer</span>
<div class="field" style="left:452px;top:123px;width:389px;height:37px"></div>
<span class="check" style="left:857px;top:135px"></span>
<span class="abs label" style="left:877px;top:135px;font-weight:500">Rate Quote?</span>

<!-- Load type tabs -->
<div class="tab active" style="left:162px;width:76px"><div class="tab-art" role="img" aria-label="Cardboard box" style="background:linear-gradient(#d9b98c,#b68f5b)"></div></div>
<div class="tab" style="left:246px;width:61px"><div class="tab-art" role="img" aria-label="Shipping container" style="left:6px;width:48px;background:linear-gradient(#4fae4b,#2f7d30)"></div></div>
<div class="tab" style="left:314px;width:62px"><div class="tab-art" role="img" aria-label="Gift parcel" style="left:6px;width:48px;background:linear-gradient(#ea4a6a,#c01e44)"></div></div>
<span class="abs link" style="left:384px;top:245px">More</span>

<section class="abs card load-panel"></section>
<span class="abs label" style="left:179px;top:308px">Qty</span>
<span class="abs label" style="left:256px;top:308px">Stackabel</span>
<span class="abs label" style="left:326px;top:308px">Load</span>
<span class="abs label" style="left:528px;top:308px">Length</span>
<span class="abs label" style="left:601px;top:308px">Width</span>
<span class="abs label" style="left:676px;top:308px">Height</span>
<span class="abs label" style="left:815px;top:308px">Weight</span>

<div class="field center" style="left:178px;top:331px;width:60px;height:31px">5</div>
<span class="check" style="left:279px;top:341px"></span>
<div class="select" style="left:324px;top:331px;width:186px;height:31px">Box/Pallet</div>
<div class="field center" style="left:526px;top:331px;width:60px;height:31px">100</div>
<div class="field center" style="left:600px;top:331px;width:60px;height:31px">100</div>
<div class="field center" style="left:674px;top:331px;width:60px;height:31px">100</div>
<div class="select" style="left:751px;top:331px;width:47px;height:31px;padding-left:9px">Cm</div>
<div class="field" style="left:814px;top:331px;width:207px;height:31px">Box/Pallet<span class="unit-tag" style="width:42px">Kg</span></div>

<div class="abs add-units">+ Add more units</div>
<div class="abs divider"></div>

<span class="abs label" style="left:559px;top:456px;font-weight:500">Total</span>
<div class="field center" style="left:596px;top:448px;width:60px;height:31px">5</div>
<div class="field" style="left:673px;top:448px;width:165px;height:31px">1<span class="unit-tag" style="width:51px">CBM</span></div>
<div class="field" style="left:854px;top:448px;width:167px;height:31px">100<span class="unit-tag" style="width:43px">Kg</span></div>

<!-- Route -->
<section class="abs route-band" role="img" aria-label="Street map of a city district"></section>
<span class="abs route-label" style="left:162px">From:</span>
<div class="field route-field" style="left:211px;width:344px">Shipping address or port</div>
<svg class="abs" style="left:599px;top:606px" width="32" height="26" viewBox="0 0 32 26" aria-hidden="true">
  <path d="M2 8h15V2l13 11-13 11v-6H2z" fill="var(--go)" stroke="#4c9410" stroke-width="1.2"/>
</svg>
<span class="abs route-label" style="left:666px">To:</span>
<div class="field route-field" style="left:694px;width:343px">Shipping address or port</div>

<!-- Options -->
<h2 class="abs options-title">Options</h2>
<span class="radio" style="left:162px"></span>
<span class="abs opt-text" style="left:182px">Import</span>
<span class="radio" style="left:238px"></span>
<span class="abs opt-text" style="left:258px">Export</span>
<span class="abs opt-text" style="left:314px">Incoterm: <span class="link" style="font-size:11.5px">FCA</span></span>

<span class="check" style="left:522px;top:764px"></span>
<svg class="hazard" style="left:539px" width="17" height="17" viewBox="0 0 17 17" aria-label="Fragile"><circle cx="8.5" cy="8.5" r="7.5" fill="#fff" stroke="var(--hazard)" stroke-width="2"/><circle cx="8.5" cy="8.5" r="3.5" fill="#222"/></svg>
<span class="check" style="left:579px;top:764px"></span>
<svg class="hazard" style="left:596px" width="17" height="17" viewBox="0 0 17 17" aria-label="Perishable"><circle cx="8.5" cy="8.5" r="7.5" fill="#fff" stroke="var(--hazard)" stroke-width="2"/><rect x="5.5" y="4" width="6" height="9" rx="1" fill="#222"/><path d="M3 3l11 11" stroke="var(--hazard)" stroke-width="2"/></svg>
<span class="check" style="left:632px;top:764px"></span>
<svg class="hazard" style="left:649px" width="17" height="17" viewBox="0 0 17 17" aria-label="Hazardous"><circle cx="8.5" cy="8.5" r="7.5" fill="#fff" stroke="var(--hazard)" stroke-width="2"/><path d="M8.5 8.5L5 3.5a6 6 0 0 1 7 0z M8.5 8.5l6 .3a6 6 0 0 1-3.5 5.8z M8.5 8.5L6 14.6a6 6 0 0 1-3.5-5.8z" fill="#222"/></svg>

<div class="select" style="left:812px;top:755px;width:225px;height:31px">Price Level</div>
<span class="abs link" style="left:955px;top:791px;font-size:11.5px">More Options</span>

<div class="abs search-button">SEARCH QUOTES</div>
<span class="abs label" style="left:629px;top:853px">or</span>
<span class="abs link" style="left:647px;top:853px;font-size:11.5px">Create Manually</span>

<!-- Footer -->
<footer class="site-footer"></footer>
<span class="abs footer-link" style="left:162px">About Us</span>
<span class="abs footer-link" style="left:223px">Privacy policy</span>
<span class="abs footer-link" style="left:308px">Terms of Service</span>
<span class="abs footer-link" style="left:407px">News</span>
<span class="social" style="left:927px"></span>
<span class="social" style="left:952px"></span>
<span class="social" style="left:974px"></span>
<span class="social" style="left:998px"></span>
<span class="social" style="left:1022px"></span>

</body>
</html>
```